KORBALT

The business want a professional looking business card. We have a scetch we will add but want the extra upgrade, and would like more suggestions for variations of our business cards.

```html
<!DOCTYPE html>
<html lang="en">
<head>
<meta charset="utf-8">
<title>KORBALT — Business Card Concepts</title>
<link rel="stylesheet" href="https://fonts.googleapis.com/css2?family=Cinzel:wght@400;500&family=Montserrat:wght@300;400;500&display=swap">
<style>
:root{
  --ink:#151515;
  --charcoal:#2a2826;
  --slate:#4a4846;
  --gold:#b8914c;
  --gold-soft:#cfae6e;
  --cream:#f1ebdf;
  --cream-deep:#ebe2d2;
  --stone:#e4ddd0;
  --stone-deep:#d8cfc0;
  --sand:#d9ccb4;
  --mist:#d6d4d2;
  --paper:#f5f3ef;
  --text:#3a3835;
  --muted:#6d6a66;
  --white:#ffffff;
}
*{margin:0;padding:0;box-sizing:border-box}
html,body{width:1200px;height:938px;overflow:hidden;background:var(--white)}
.board{position:relative;width:1200px;height:938px}
.concept{position:absolute;top:80px;width:396px;height:801px}
.concept--one{left:0}
.concept--two{left:403px;width:395px}
.concept--three{left:804px}
.stage{position:relative;height:508px}
.concept--one .stage{background:#e6d9c6}
.concept--two .stage{background:#3b3835}
.concept--three .stage{background:#e2d9cb}
.card{position:absolute;left:48px;width:300px;height:172px;overflow:hidden;box-shadow:0 6px 18px rgba(0,0,0,.18)}
.card--front{top:48px}
.card--back{top:282px}
.card--black{background:var(--ink)}
.card--cream{background:var(--cream)}
.card--stone{background:var(--stone)}
.ornament-area{position:absolute;top:0;bottom:0;right:0}
.ornament-area--cream{width:120px;background:linear-gradient(90deg,var(--cream),var(--cream-deep))}
.ornament-area--stone{width:90px;background:linear-gradient(90deg,var(--stone),var(--stone-deep))}
.wordmark{font-family:"Cinzel",serif;font-weight:400;color:var(--gold);letter-spacing:.18em}
.tagline{font-family:"Montserrat",sans-serif;font-weight:400;color:var(--gold);letter-spacing:.45em;font-size:7px}
.front-lockup{position:absolute;inset:0;display:flex;flex-direction:column;align-items:center;justify-content:center;gap:8px}
.front-lockup .wordmark{font-size:30px}
.deco{position:absolute;inset:0;width:100%;height:100%}
.details{position:absolute;left:22px;top:30px;font-family:"Montserrat",sans-serif}
.person{font-family:"Cinzel",serif;font-size:12px;letter-spacing:.08em;color:var(--ink)}
.role{font-size:8px;color:var(--muted);margin-top:6px}
.rule{width:28px;height:1px;background:var(--gold);margin:14px 0 16px}
.contact{list-style:none;font-size:8px;color:var(--text)}
.contact li{display:flex;align-items:center;gap:8px;margin-bottom:7px}
.contact svg{width:9px;height:9px;flex:none}
.card--black .person,.card--black .role,.card--black .contact{color:var(--gold-soft)}
.back-lockup{position:absolute;right:16px;bottom:40px;display:flex;flex-direction:column;align-items:center;gap:5px}
.back-lockup .wordmark{font-size:12px}
.back-lockup .tagline{font-size:5px}
.lockup-dot{width:16px;height:16px;border-radius:50%;border:1px solid var(--gold);margin-bottom:4px}
.divider{position:absolute;top:26px;bottom:26px;left:196px;width:1px;background:var(--gold)}
.gold-line{position:absolute;top:0;bottom:0;right:14px;width:1px;background:var(--gold)}
.tiles{display:flex;height:132px}
.tile{position:relative;overflow:hidden;display:flex;flex-direction:column;align-items:center;justify-content:center;gap:10px}
.tile--wide{width:217px}
.tile--narrow{flex:1;border-left:2px solid var(--white)}
.tile .wordmark{font-size:26px}
.tile .wordmark--small{font-size:13px}
.tile-circle{width:30px;height:30px;border-radius:50%;background:var(--gold)}
.caption{position:relative;height:161px;background:var(--paper);padding:22px 34px 0 34px;font-family:"Montserrat",sans-serif}
.concept-label{font-size:10px;font-weight:500;letter-spacing:.32em;color:var(--ink)}
.concept-title{font-size:10px;font-weight:400;letter-spacing:.2em;color:var(--ink);margin-top:12px;line-height:1.35}
.concept-copy{font-size:9.5px;font-weight:300;color:var(--muted);line-height:1.65;margin-top:8px;max-width:290px}
.caption-rule{width:48px;height:1px;background:var(--slate);margin-top:14px}
.swatches{position:absolute;top:22px;right:28px;display:flex;gap:8px;list-style:none}
.swatches li{width:20px;height:20px;border-radius:50%}
</style>
</head>
<body>
<main class="board">

  <section class="concept concept--one">
    <div class="stage">
      <div class="card card--front card--black">
        <div class="front-lockup">
          <span class="wordmark">KORBALT</span>
          <span class="tagline">SINCE 2026</span>
        </div>
      </div>
      <div class="card card--back card--cream">
        <div class="ornament-area ornament-area--cream" role="img" aria-label="Fine organic gold line ornament"></div>
        <div class="details">
          <p class="person">KORBALT RAVNSBORG</p>
          <p class="role">CEO &amp; Founder</p>
          <div class="rule"></div>
          <ul class="contact">
            <li><svg viewBox="0 0 10 10"><rect x="2.5" y=".5" width="5" height="9" rx="1" fill="none" stroke="#b8914c"/></svg>004791234570</li>
            <li><svg viewBox="0 0 10 10"><rect x=".5" y="2" width="9" height="6" fill="#b8914c"/><path d="M.5 2 L5 5.5 L9.5 2" fill="none" stroke="#f1ebdf" stroke-width=".8"/></svg>korbalt.llc@mailbox.com</li>
            <li><svg viewBox="0 0 10 10"><circle cx="5" cy="5" r="4.3" fill="none" stroke="#b8914c"/><path d="M.7 5 H9.3 M5 .7 C2.5 3 2.5 7 5 9.3 M5 .7 C7.5 3 7.5 7 5 9.3" fill="none" stroke="#b8914c" stroke-width=".7"/></svg>www.korbalt.llc</li>
          </ul>
        </div>
        <div class="back-lockup">
          <span class="lockup-dot"></span>
          <span class="wordmark">KORBALT</span>
          <span class="tagline">SINCE 2026</span>
        </div>
      </div>
    </div>
    <div class="tiles">
      <div class="tile tile--wide" style="background:var(--ink)"><span class="wordmark">KORBALT</span></div>
      <div class="tile tile--narrow" style="background:var(--cream)"><span class="tile-circle"></span><span class="wordmark wordmark--small">KORBALT</span></div>
    </div>
    <div class="caption">
      <p class="concept-label">CONCEPT 1</p>
      <h2 class="concept-title">HERITAGE MINIMALIST<br>WITH A MODERN TWIST</h2>
      <p class="concept-copy">Clean, timeless and professional with a refined symbol and subtle organic lines. Elegant, confident and memorable.</p>
      <div class="caption-rule"></div>
      <ul class="swatches">
        <li style="background:var(--ink)"></li>
        <li style="background:var(--gold)"></li>
        <li style="background:var(--cream)"></li>
      </ul>
    </div>
  </section>

  <section class="concept concept--two">
    <div class="stage">
      <div class="card card--front card--black">
        <svg class="deco" viewBox="0 0 300 172" aria-hidden="true">
          <polygon points="300,40 300,172 210,172" fill="#2a2826"/>
          <polygon points="300,40 300,58 222,172 210,172" fill="#b8914c"/>
        </svg>
        <div class="front-lockup">
          <span class="wordmark">KORBALT</span>
          <span class="tagline">SINCE 2026</span>
        </div>
      </div>
      <div class="card card--back card--black">
        <div class="details">
          <p class="person">KORBALT RAVNSBORG</p>
          <p class="role">CEO &amp; Founder</p>
          <div class="rule"></div>
          <ul class="contact">
            <li><svg viewBox="0 0 10 10"><rect x="2.5" y=".5" width="5" height="9" rx="1" fill="none" stroke="#cfae6e"/></svg>004791234570</li>
            <li><svg viewBox="0 0 10 10"><rect x=".5" y="2" width="9" height="6" fill="#cfae6e"/><path d="M.5 2 L5 5.5 L9.5 2" fill="none" stroke="#151515" stroke-width=".8"/></svg>korbalt.llc@mailbox.com</li>
            <li><svg viewBox="0 0 10 10"><circle cx="5" cy="5" r="4.3" fill="none" stroke="#cfae6e"/><path d="M.7 5 H9.3 M5 .7 C2.5 3 2.5 7 5 9.3 M5 .7 C7.5 3 7.5 7 5 9.3" fill="none" stroke="#cfae6e" stroke-width=".7"/></svg>www.korbalt.llc</li>
          </ul>
        </div>
        <div class="divider"></div>
        <div class="back-lockup" style="right:14px;bottom:48px">
          <span class="lockup-dot"></span>
          <span class="wordmark">KORBALT</span>
          <span class="tagline">SINCE 2026</span>
        </div>
      </div>
    </div>
    <div class="tiles">
      <div class="tile tile--wide" style="background:var(--ink)"><span class="tile-circle"></span><span class="wordmark wordmark--small">KORBALT</span></div>
      <div class="tile tile--narrow" style="background:var(--charcoal)">
        <svg class="deco" viewBox="0 0 178 132" aria-hidden="true">
          <polygon points="0,0 96,0 40,132 0,132" fill="#151515"/>
          <polygon points="96,0 106,0 50,132 40,132" fill="#b8914c"/>
        </svg>
      </div>
    </div>
    <div class="caption">
      <p class="concept-label">CONCEPT 2</p>
      <h2 class="concept-title">SOPHISTICATED DARK ELEGANCE</h2>
      <p class="concept-copy">Bold, premium and distinctive. A refined dark palette with precise gold detailing creates a powerful first impression while staying professional and timeless.</p>
      <div class="caption-rule"></div>
      <ul class="swatches">
        <li style="background:var(--ink)"></li>
        <li style="background:var(--gold)"></li>
        <li style="background:var(--slate)"></li>
      </ul>
    </div>
  </section>

  <section class="concept concept--three">
    <div class="stage">
      <div class="card card--front card--stone">
        <div class="ornament-area ornament-area--stone" role="img" aria-label="Soft tonal wave texture"></div>
        <div class="gold-line"></div>
        <div class="front-lockup">
          <span class="wordmark">KORBALT</span>
          <span class="tagline">SINCE 2026</span>
        </div>
      </div>
      <div class="card card--back card--stone">
        <div class="ornament-area ornament-area--stone" role="img" aria-label="Soft tonal wave texture"></div>
        <div class="details">
          <p class="person">KORBALT RAVNSBORG</p>
          <p class="role">CEO &amp; Founder</p>
          <div class="rule"></div>
          <ul class="contact">
            <li><svg viewBox="0 0 10 10"><rect x="2.5" y=".5" width="5" height="9" rx="1" fill="none" stroke="#151515"/></svg>004791234570</li>
            <li><svg viewBox="0 0 10 10"><rect x=".5" y="2" width="9" height="6" fill="#151515"/><path d="M.5 2 L5 5.5 L9.5 2" fill="none" stroke="#e4ddd0" stroke-width=".8"/></svg>korbalt.llc@mailbox.com</li>
            <li><svg viewBox="0 0 10 10"><circle cx="5" cy="5" r="4.3" fill="none" stroke="#151515"/><path d="M.7 5 H9.3 M5 .7 C2.5 3 2.5 7 5 9.3 M5 .7 C7.5 3 7.5 7 5 9.3" fill="none" stroke="#151515" stroke-width=".7"/></svg>www.korbalt.llc</li>
          </ul>
        </div>
        <div class="divider"></div>
        <div class="back-lockup" style="right:14px;bottom:48px">
          <span class="lockup-dot"></span>
          <span class="wordmark">KORBALT</span>
          <span class="tagline">SINCE 2026</span>
        </div>
      </div>
    </div>
    <div class="tiles">
      <div class="tile tile--wide" style="background:var(--stone)"><span class="wordmark">KORBALT</span></div>
      <div class="tile tile--narrow" role="img" aria-label="Close-up of embossed wave texture" style="background:linear-gradient(135deg,var(--stone-deep),var(--stone))"></div>
    </div>
    <div class="caption">
      <p class="concept-label">CONCEPT 3</p>
      <h2 class="concept-title">CONTEMPORARY TEXTURE &amp; TYPOGRAPHY</h2>
      <p class="concept-copy">Modern, refined and unique. The custom monogram and textured background add character, making it stand out in a sophisticated way.</p>
      <div class="caption-rule"></div>
      <ul class="swatches">
        <li style="background:var(--sand)"></li>
        <li style="background:var(--gold)"></li>
        <li style="background:var(--mist)"></li>
      </ul>
    </div>
  </section>

</main>
</body>
</html>
```